Digital Agency Needs a Relaunch

We are looking for a modern, top-notch design to elevate our brand to win new clients. It has to build on the clarity of message in the current wireframes and must fit together well on Wordpress.

The winning designer will need to complete the other pages, but please focus on the homepage as the base of your proposed designs for us.

Use the existing logo as a point, and the colour scheme should be around that, we currently use these colours, but you can suggest new mixes:
Purple: #5c306b
Orange: #e27927
Grey: #5f4f61
Light grey: #cacaca
Off white: #ececec
Blue: #674ea7
Updates

Target Market(s)

Decent Sized SME Businesses (20+ Staff, Over £1m turnover)

Industry/Entity Type

Digital Marketing

Number of Pages Required

5+ page

Font styles to use
Sans Serif

Colors

Designer to choose colors to be used in the design.

Requirements
Must have
• A real attention on the design piece. Ignore the current website and really focus on the messaging and the brief.
Nice to have
• Read the messages and think about the impact. Use the purple in the logo more than the orange, but try to keep it smart rather than cool
Should not have
• Inconsistent design, serif fonts, stock images and not meeting the wireframes.

```html
<!DOCTYPE html>
<html lang="en">
<head>
<meta charset="utf-8">
<title>Vectra Digital – Growth Works For You</title>
<link href="https://fonts.googleapis.com/css2?family=Lexend:wght@400;500;600;700&family=Lato:wght@400;700&display=swap" rel="stylesheet">
<style>
:root{
  --purple:#5c306b;
  --purple-deep:#221042;
  --navy:#1b0f3d;
  --orange:#f2621f;
  --orange-soft:#f58a3a;
  --grey:#5f4f61;
  --light:#f4f3f6;
  --ink:#1f1b24;
  --cyan:#13b2cb;
  --indigo:#2e2b6e;
  --slate:#394452;
  --red:#f04a22;
  --footer:#1d1b20;
  --white:#fff;
}
*{box-sizing:border-box;margin:0;padding:0}
html,body{width:1200px;height:4461px;overflow:hidden}
body{font-family:"Lato",sans-serif;color:var(--ink);background:var(--white);position:relative}
h1,h2,h3,h4,.btn,.nav,.brand{font-family:"Lexend",sans-serif}
section,header,footer{position:absolute;left:0;width:1200px}
.btn{display:inline-flex;align-items:center;justify-content:center;gap:10px;border-radius:30px;font-weight:500;font-size:19px;text-decoration:none}
.btn-orange{background:var(--orange);color:var(--white)}
.btn-white{background:var(--white);color:var(--orange)}

/* header */
.site-header{top:0;height:135px;background:var(--white)}
.brand{position:absolute;left:111px;top:30px;display:flex;align-items:center;gap:10px;color:var(--purple);font-weight:500;font-size:34px;letter-spacing:.5px}
.brand-dot{width:22px;height:22px;border-radius:50%;border:4px solid var(--orange)}
.topbar{position:absolute;left:343px;top:0;width:857px;height:59px;background:var(--purple);border-bottom-left-radius:30px;display:flex;align-items:center;color:var(--white);font-size:17px;font-family:"Lexend",sans-serif}
.topbar span{position:absolute;top:19px}
.phone-ic{position:absolute;left:557px;top:11px;width:38px;height:38px;border-radius:50%;background:var(--orange);display:flex;align-items:center;justify-content:center}
.nav{position:absolute;top:88px;left:0;width:100%;font-size:18px;color:var(--ink)}
.nav span{position:absolute}

/* hero */
.hero{top:135px;height:540px;overflow:hidden}
.hero-bg{position:absolute;inset:0;background:linear-gradient(110deg,#1c0e3c 0%,#2d1256 55%,#3f1a6a 80%,#25103f 100%);border-bottom-left-radius:170px}
.hero h1{position:absolute;left:108px;top:168px;font-size:68px;line-height:86px;font-weight:600;color:var(--white)}
.hero h1 em{font-style:normal;color:var(--orange)}

/* intro */
.intro{top:675px;height:468px;text-align:center}
.intro h2{margin-top:60px;font-size:40px;font-weight:500;line-height:58px}
.intro h2 .sub{display:block;color:var(--purple)}
.intro p{width:810px;margin:20px auto 0;font-size:14.5px;line-height:29px;color:#333}
.intro .cta-row{margin-top:26px;display:flex;justify-content:center;align-items:center;gap:40px}
.intro .link{font-family:"Lexend",sans-serif;color:var(--purple);font-size:20px;font-weight:500}
.intro .btn{width:170px;height:50px}

/* services */
.services{top:1143px;height:447px;background:var(--light)}
.svc{position:absolute;top:100px;width:212px;height:267px;background:var(--purple);border-radius:12px;color:var(--white);text-align:center}
.svc-icon{position:absolute;left:61px;top:-30px;width:90px;height:90px;border-radius:50%;background:var(--purple);border:5px solid var(--white);display:flex;align-items:center;justify-content:center}
.svc h3{margin-top:80px;font-size:22px;font-weight:600;letter-spacing:.5px}
.svc ul{list-style:none;margin-top:12px;font-size:15px;font-weight:700;line-height:33px}
.svc li::before{content:"→ ";}

/* pain / gain */
.paingain{top:1590px;height:462px}
.pg-card{position:absolute;width:459px;height:228px;color:var(--white);text-align:center}
.pg-card h3{font-size:22px;font-weight:600;padding-top:50px}
.pg-card p{font-size:16.5px;line-height:33px;margin-top:14px;font-weight:700}
.pain{left:111px;top:73px;background:var(--grey);border-top-left-radius:50px;border-bottom-right-radius:60px;box-shadow:-6px 6px 0 var(--orange)}
.gain{left:629px;top:65px;background:var(--purple);border-top-left-radius:50px;border-bottom-right-radius:60px;box-shadow:6px -6px 0 var(--orange)}
.gain h3{padding-top:42px}
.gain p{margin-top:8px}
.ctrl{position:absolute;top:330px;width:56px;height:56px;border-radius:50%;background:var(--white);box-shadow:0 3px 10px rgba(0,0,0,.15);display:flex;align-items:center;justify-content:center}
.paingain .btn{position:absolute;left:769px;top:332px;width:170px;height:50px}

/* about */
.about{top:2052px;height:575px;background:var(--light)}
.about h2{text-align:center;margin-top:75px;font-size:40px;font-weight:500;color:var(--grey)}
.about-text{position:absolute;left:111px;top:170px;width:480px;font-size:14.5px;line-height:29px;color:#333}
.about-text p+p{margin-top:29px}
.about-frame{position:absolute;left:663px;top:156px;width:425px;height:333px;border-top:5px solid var(--purple);border-left:5px solid var(--purple);border-right:5px solid var(--orange);border-bottom:5px solid var(--orange);border-top-left-radius:40px;border-bottom-right-radius:60px}
.about-photo{position:absolute;left:8px;top:8px;right:8px;bottom:8px;border-top-left-radius:32px;border-bottom-right-radius:52px;background:radial-gradient(circle at 75% 20%,#f7e9a0 0%,#b7c24a 25%,#4f6a1f 55%,#3a2614 85%)}

/* case studies */
.cases{top:2627px;height:496px}
.cases h2{text-align:center;margin-top:66px;font-size:40px;font-weight:500}
.cases h2 span{color:var(--purple)}
.case{position:absolute;top:156px;width:223px;height:264px;border-radius:16px;color:var(--white);text-align:center;padding:14px}
.case-logo{height:110px;background:var(--white);border-radius:14px;display:flex;align-items:center;justify-content:center;font-family:"Lexend",sans-serif;font-weight:600;font-size:22px;gap:8px}
.case-logo i{width:16px;height:16px;border-radius:50%;display:inline-block}
.case p{margin-top:24px;font-size:13px;line-height:26px}

/* cta band */
.boost{top:3123px;height:334px;background:linear-gradient(120deg,#ee6a24 0%,#e9531f 50%,#f06b2b 100%);text-align:center;color:var(--white)}
.boost h2{margin-top:68px;font-size:40px;font-weight:500;line-height:56px}
.boost .btn{margin-top:34px;width:255px;height:48px}

/* blog */
.blog{top:3457px;height:499px}
.blog-curve{position:absolute;left:0;top:300px;width:200px;height:200px;background:var(--footer)}
.blog-curve::after{content:"";position:absolute;inset:0;background:var(--white);border-bottom-left-radius:170px}
.blog h2{position:relative;text-align:center;margin-top:70px;font-size:40px;font-weight:500;color:var(--purple)}
.blog h2 span{color:var(--ink)}
.post{position:absolute;top:158px;width:223px}
.post-img{height:222px;border-radius:14px 14px 0 0;background:linear-gradient(160deg,#d7dbe2 0%,#9aa4b3 50%,#5a6270 100%)}
.post-cap{position:relative;margin:-30px 20px 0;background:var(--white);border-radius:14px 14px 0 0;text-align:center;font-size:14px;line-height:26px;padding-top:4px;font-family:"Lexend",sans-serif;font-weight:400}

/* footer */
.site-footer{top:3956px;height:505px;background:var(--footer);color:var(--white)}
.fcol{position:absolute;top:72px}
.fcol h4{font-size:21px;font-weight:500}
.fcol ul{list-style:none;margin-top:10px;font-size:14px;line-height:34.5px;color:#e6e3ea}
.fcol li::before{content:"»";margin-right:18px}
.contact-box{position:absolute;left:111px;top:284px;width:977px;height:107px;border:1px solid #3a373f;display:flex}
.contact-box div{position:relative;border-right:1px solid #3a373f;display:flex;align-items:center;gap:22px;padding-left:22px;font-size:12px;line-height:20px}
.contact-box div:last-child{border-right:none}
.contact-box b{display:block;font-family:"Lexend",sans-serif;font-weight:400;font-size:15px;margin-bottom:4px}
.legal{position:absolute;top:450px;left:111px;right:111px;font-size:13px;display:flex;justify-content:space-between}
.legal span+span{margin-left:26px}
</style>
</head>
<body>

<header class="site-header">
  <div class="brand"><span class="brand-dot"></span>vectra digital</div>
  <div class="topbar">
    <span style="left:60px">Blog</span>
    <span style="left:160px">|</span>
    <span style="left:226px">About Us</span>
    <span style="left:350px">|</span>
    <span style="left:417px">Contact Us</span>
    <div class="phone-ic"><svg width="18" height="18" viewBox="0 0 24 24" fill="#fff"><path d="M6.6 10.8a15.1 15.1 0 006.6 6.6l2.2-2.2c.3-.3.7-.4 1-.2 1.1.4 2.3.6 3.6.6.6 0 1 .4 1 1V20c0 .6-.4 1-1 1A17 17 0 013 4c0-.6.4-1 1-1h3.5c.6 0 1 .4 1 1 0 1.3.2 2.5.6 3.6.1.3 0 .7-.2 1z"/></svg></div>
    <span style="left:612px;font-size:18px">01632 480 219</span>
  </div>
  <nav class="nav">
    <span style="left:377px">Create</span>
    <span style="left:509px">Communicate</span>
    <span style="left:709px">Convert</span>
    <span style="left:851px">Close</span>
    <span style="left:972px">Case Studies</span>
  </nav>
</header>

<section class="hero">
  <svg width="1200" height="540" style="position:absolute;left:0;top:0">
    <path d="M0 360 C0 470 70 540 180 540 L0 540Z" fill="var(--orange)"/>
  </svg>
  <div class="hero-bg" role="img" aria-label="Dark purple backdrop with rising growth arrows"></div>
  <h1>Growth Works<br><em>For You</em></h1>
</section>

<section class="intro">
  <h2>Fed Up With Agencies Who Don't Care?<span class="sub">We've Heard That Before</span></h2>
  <p>We know every client has unique needs. Yet, few digital agencies spend enough time getting to know the client's business. We're different. We take a highly personalised approach to every project, working closely with our clients to understand their objectives, challenges, and target audience.</p>
  <p style="margin-top:29px">Knowing your business is the first step in helping you grow. It's how we work, and it will work for you.</p>
  <div class="cta-row"><span class="link">Achieve Growth That Works</span><a class="btn btn-orange">Set Up a Call</a></div>
</section>

<section class="services">
  <div class="svc" style="left:111px">
    <div class="svc-icon"><svg width="40" height="40" viewBox="0 0 40 40" fill="none" stroke="#fff" stroke-width="2.4"><rect x="6" y="12" width="22" height="22" rx="3"/><rect x="12" y="6" width="22" height="22" rx="3"/><path d="M23 12v12M17 18h12"/></svg></div>
    <h3>CREATE</h3><ul><li>Branding</li><li>Graphics</li><li>Video</li><li>Content</li></ul>
  </div>
  <div class="svc" style="left:367px">
    <div class="svc-icon"><svg width="42" height="40" viewBox="0 0 42 40" fill="none" stroke="#fff" stroke-width="2.4"><path d="M14 10a12 9 0 1124 0 12 9 0 01-17 8l-5 3 1-5"/><path d="M10 16a10 8 0 1012 12l5 3-1-5"/><path d="M8 24h6M8 28h8"/></svg></div>
    <h3>COMMUNICATE</h3><ul><li>Ads</li><li>Organic</li><li>Social</li><li>Email</li></ul>
  </div>
  <div class="svc" style="left:622px">
    <div class="svc-icon"><svg width="40" height="40" viewBox="0 0 40 40" fill="none" stroke="#fff" stroke-width="2.4"><rect x="4" y="10" width="16" height="22" rx="2"/><rect x="20" y="6" width="16" height="22" rx="2"/><path d="M8 16h8M8 21h8M24 12h8M24 17h8M24 22h6"/></svg></div>
    <h3>CONVERT</h3><ul><li>Websites</li><li>Lead Generation</li><li>E-commerce</li><li>Analytics</li></ul>
  </div>
  <div class="svc" style="left:877px">
    <div class="svc-icon"><svg width="42" height="40" viewBox="0 0 42 40" fill="none" stroke="#fff" stroke-width="2.4"><path d="M3 16l8-8 7 3 6-2 8 8-12 12-3-3"/><path d="M39 16l-8-8M18 11l-6 7 3 3 6-5 9 8"/><path d="M14 26l3 3M17 23l4 4"/></svg></div>
    <h3>CLOSE</h3><ul><li>CRM</li><li>Systems</li><li>Customer Success</li><li>AI &amp; Automations</li></ul>
  </div>
</section>

<section class="paingain">
  <div class="pg-card pain"><h3>YOUR PAIN?</h3><p>"I spend most of my development budget<br>fixing errors and bugs"</p></div>
  <div class="pg-card gain"><h3>FUTURE GAIN</h3><p>A fast and reliable cash- generative<br>content-manager e-commerce or lead<br>generation website</p></div>
  <div class="ctrl" style="left:274px"><svg width="16" height="18"><rect x="1" y="0" width="5" height="18" fill="#111"/><rect x="10" y="0" width="5" height="18" fill="#111"/></svg></div>
  <div class="ctrl" style="left:359px"><svg width="16" height="18"><path d="M2 0L16 9 2 18Z" fill="#111"/></svg></div>
  <a class="btn btn-orange">Websites</a>
</section>

<section class="about">
  <h2>Vectra: Where Growth Works</h2>
  <div class="about-text">
    <p>We understand the importance of a strong on line presence. That's why we offer a complete range of digital marketing solutions to help you reach your growth goals. Our track record demonstrates expertise in all forms of digital marketing website builds, Searchly Ads, SEO, Email Marketing.</p>
    <p>We're constantly staying up-to-date on the latest trends, tech and best practices in the industry, so you can trust that you're getting the most effective and efficient strategies for your business growth.<br>Set up a call and we're confident we can show you where we can add growth and value to your business.</p>
  </div>
  <div class="about-frame"><div class="about-photo" role="img" aria-label="Young green seedling sprouting from soil in warm sunlight"></div></div>
</section>

<section class="cases">
  <h2>Case <span>Studies</span></h2>
  <div class="case" style="left:111px;background:var(--cyan)"><div class="case-logo" style="color:#1c2a5a"><i style="background:var(--cyan)"></i>Corvane</div><p>Temporibus autem quibus dam et aut officiis debitis aut rerum necessitaepe eveniet ut et voluptates</p></div>
  <div class="case" style="left:362px;background:var(--indigo)"><div class="case-logo" style="color:#f0a21c">Pliant Rooms</div><p>Itaque earum rerum hic tenetur a sapiente delectus, ut aut reiciendis voluptatibus maiores</p></div>
  <div class="case" style="left:613px;background:var(--slate)"><div class="case-logo" style="color:var(--slate)">Ostrel</div><p>Nam libero tempore, cum soluta nobis est eligendi optio cumque nihil impedit quo minus</p></div>
  <div class="case" style="left:864px;background:var(--red)"><div class="case-logo" style="color:#4a4a4a;font-size:19px"><i style="background:var(--red)"></i>Meridel Marine</div><p>Optio cumque nihil impedit quo minus id quod maxime placeat facere possimus, omnis voluptas assumenda</p></div>
</section>

<section class="boost">
  <h2>We're the turbo boost for your digital<br>marketing engine</h2>
  <a class="btn btn-white">Put Your Foot Down <svg width="20" height="16" viewBox="0 0 20 16"><path d="M0 7L20 0 14 16 10 10Z" fill="var(--orange)"/></svg></a>
</section>

<section class="blog">
  <div class="blog-curve"></div>
  <h2>From <span>The</span> Blog</h2>
  <div class="post" style="left:111px"><div class="post-img" role="img" aria-label="Team gathered around a laptop in an office"></div><div class="post-cap">Searchly's New PPC Features<br>are Loaded with AI</div></div>
  <div class="post" style="left:362px"><div class="post-img" role="img" aria-label="Smiling professional in an office setting"></div><div class="post-cap">How Searchly Killed<br>the Broad Match<br>Keyword?</div></div>
  <div class="post" style="left:613px"><div class="post-img" role="img" aria-label="Colleagues celebrating in a meeting"></div><div class="post-cap">The 9 Rules of Social<br>Media Engagement<br>(Part II)</div></div>
  <div class="post" style="left:864px"><div class="post-img" role="img" aria-label="Cheerful team working together at a desk"></div><div class="post-cap">The 9 Rules of Social<br>Media Engagement<br>(Part I)</div></div>
</section>

<footer class="site-footer">
  <div class="fcol" style="left:111px"><h4>Create</h4><ul><li>Branding</li><li>Graphics</li><li>Video</li><li>Content</li></ul></div>
  <div class="fcol" style="left:280px"><h4>Convert</h4><ul><li>Websites</li><li>Lead Generation</li><li>Ecommerce</li><li>Analytics</li></ul></div>
  <div class="fcol" style="left:496px"><h4>Communicate</h4><ul><li>Ads</li><li>Organic</li><li>Social</li><li>Email</li></ul></div>
  <div class="fcol" style="left:718px"><h4>Close</h4><ul><li>CRM</li><li>Systems</li><li>Customer Success</li><li>AI &amp; Automations</li></ul></div>
  <div class="fcol" style="left:955px"><h4>Connect</h4><ul><li>Case Studies</li><li>Blog</li><li>About Us</li></ul></div>
  <div class="contact-box">
    <div style="width:326px"><svg width="56" height="56" viewBox="0 0 56 56" fill="none" stroke="#fff" stroke-width="2"><rect x="6" y="22" width="18" height="30"/><rect x="24" y="8" width="22" height="44"/><path d="M10 28h4M16 28h4M10 36h4M16 36h4M29 14h4M37 14h4M29 22h4M37 22h4M29 30h4M37 30h4M31 52v-10h8v10M2 52h52"/></svg><p><b>ADDRESS :</b>Harbour Mill House<br>Eastbrook Shire, EB4 2QT</p></div>
    <div style="width:370px;padding-left:40px"><svg width="56" height="40" viewBox="0 0 56 40" fill="none" stroke="#fff" stroke-width="2.4"><rect x="2" y="2" width="52" height="36" rx="2"/><path d="M2 4l26 20L54 4M2 38l20-18M54 38L34 20"/></svg><p><b>EMAIL US :</b>hello@vectradigital.example</p></div>
    <div style="flex:1;padding-left:50px"><svg width="56" height="56" viewBox="0 0 56 56" fill="none" stroke="#fff" stroke-width="2"><path d="M10 6l8 0 4 12-6 4a30 30 0 0016 16l4-6 12 4v8c0 3-3 6-6 6A44 44 0 014 12c0-3 3-6 6-6z"/><path d="M32 6a18 18 0 0118 18M32 14a10 10 0 0110 10"/></svg><p><b>CONTACT US</b>01632 480 219</p></div>
  </div>
  <div class="legal"><span>© Copyright 2023 Vectra Digital Limited | All Rights Reserved.</span><span><span>Site Map</span><span>Terms Of Use</span><span>Privacy Policy</span></span></div>
</footer>

</body>
</html>
```